Trvmlegal.com needs a wedsite. Law Office of Darnell P. Whitby

Darnell P. Whitby is a criminal law firm that is 5 years old. We have already had all the content written and now just need the website designed. We also just finished our logo design using Pixel Harbor and would like it used in the design of the website.

Industry/Entity Type

Law Firm

Number of Pages Required

5+ page

Requirements
Must have
• I was our new logo to be on the website also. I want Dallas sites as the stock pictures for the website. For example the Grey Stone Tribunal. I also need to be able to add YouTube videos. It has to adjust to be seen on computers and also cell phones. I need to be able to have a information sheet for clients to fill out and submit back to me.

```html
<!DOCTYPE html>
<html lang="en">
<head>
<meta charset="utf-8">
<title>Law Office of Darnell P. Whitby</title>
<link rel="stylesheet" href="https://fonts.googleapis.com/css2?family=Merriweather:wght@300;400;700&family=Open+Sans:wght@400;600&display=swap">
<style>
:root{
  --navy:#0c3679;
  --charcoal:#3d3d3d;
  --footer:#393939;
  --field:#4a4a4a;
  --coral:#d4585a;
  --slate:#4b4b4b;
  --page:#f4f4f4;
  --rule:#d6d6d6;
  --rule-strong:#c9c9c9;
  --text:#7a7a7a;
  --muted:#8d8d8d;
  --white:#ffffff;
  --tab:#c6c6c6;
}
*{margin:0;padding:0;box-sizing:border-box}
html,body{width:722px;height:1200px;overflow:hidden}
body{position:relative;background:var(--page);font-family:"Open Sans",Arial,sans-serif;color:var(--text)}
.abs{position:absolute}
.serif{font-family:"Merriweather",Georgia,serif}

/* header */
.site-header{left:0;top:0;width:722px;height:68px;background:var(--charcoal)}
.brand{left:152px;top:14px;width:100px;color:var(--white);font-family:"Merriweather",Georgia,serif;font-size:10px;line-height:14px;font-weight:400}
.brand-divider{left:260px;top:15px;width:1px;height:25px;background:#2a2a2a}
.tagline{left:274px;top:15px;font-family:"Merriweather",Georgia,serif;font-size:8px;line-height:13px;color:#777;font-weight:300}
.contact-box{left:467px;top:14px;width:107px;height:24px;background:#333;border-radius:2px;padding:2px 6px;font-size:7.2px;line-height:10px;color:#cfcfcf}
.contact-box div{display:flex;align-items:center;gap:5px}

/* nav */
.main-nav{left:0;top:68px;width:722px;height:39px;background:var(--white)}
.nav-item{top:14px;font-family:"Merriweather",Georgia,serif;font-size:7.8px;color:#888}
.nav-item.active{color:var(--navy)}
.nav-bar{top:36px;height:3px;background:var(--rule-strong)}
.dropdown{left:295px;top:108px;width:91px;background:var(--white);border:1px solid #ccc;z-index:3}
.dropdown div{border-bottom:1px solid #ddd;padding:4px 5px;font-family:"Merriweather",Georgia,serif;font-size:6.5px;line-height:9.5px;color:#666}
.dropdown div:last-child{border-bottom:none}

/* hero */
.hero{left:0;top:107px;width:722px;height:233px;background:linear-gradient(180deg,#b9cbe0 0%,#c7d3de 35%,#a7866e 60%,#8a5a3a 80%,#5f5a48 100%)}

/* practice cards */
.slide-arrow{width:11px;height:11px;border-radius:1px;display:flex;align-items:center;justify-content:center}
.card{top:366px;width:135px;height:100px;border-radius:2px;color:var(--white);text-align:center;padding-top:10px}
.card h3{font-family:"Merriweather",Georgia,serif;font-size:10.8px;line-height:14px;font-weight:700;margin-bottom:7px}
.card p{font-family:"Merriweather",Georgia,serif;font-size:6.8px;line-height:10px;padding:0 12px;height:32px}
.card span{display:block;margin-top:7px;font-family:"Merriweather",Georgia,serif;font-size:7px}
.card-navy{left:149px;background:var(--navy)}
.card-slate{left:293px;background:var(--slate)}
.card-coral{left:438px;background:var(--coral)}

/* section headings */
.section-title{font-family:"Merriweather",Georgia,serif;font-size:9px;color:#6a6a6a;font-weight:300}
.section-rule{height:1px;background:#e4e4e4}
.section-rule-accent{height:3px;background:var(--rule)}

/* team */
.team-card{top:533px;width:132px;height:82px;border-radius:1px}
.team-lead{left:149px;background:#dcdcdc;text-align:center;padding-top:30px}
.team-lead .name{font-family:"Merriweather",Georgia,serif;font-size:8.5px;color:var(--navy)}
.team-lead .role{font-family:"Merriweather",Georgia,serif;font-size:6px;color:#777;margin-top:4px}
.photo-a{left:294px;background:linear-gradient(160deg,#8a9a4e,#b8a27b 55%,#6f7c3a)}
.photo-b{left:441px;background:linear-gradient(90deg,#7a6a4a,#4b4c55 45%,#6b5533 75%,#3b2a1c)}
.team-tab{left:149px;width:135px;height:27px;border-radius:2px;padding-left:9px;display:flex;align-items:center;font-family:"Merriweather",Georgia,serif;font-size:8.8px;color:#555;background:var(--tab)}
.team-tab.active{background:var(--navy);color:var(--white)}
.bio-name{left:306px;top:637px;font-family:"Merriweather",Georgia,serif;font-size:16px;color:#555;font-weight:400}
.bio-text{left:306px;top:665px;width:268px;font-size:6.5px;line-height:10.2px;color:#888}
.btn{background:var(--navy);color:var(--white);font-family:"Merriweather",Georgia,serif;border-radius:2px;text-align:center}

/* news & video */
.date-box{left:149px;top:891px;width:29px;height:31px;background:#5e5e5e;color:var(--white);text-align:center;font-family:"Merriweather",Georgia,serif}
.date-box .day{font-size:11px;line-height:14px;padding-top:2px;font-weight:700}
.date-box .mon{font-size:5.5px;line-height:7px;color:#ccc}
.news-title{left:184px;top:890px;width:180px;font-family:"Merriweather",Georgia,serif;font-size:9.5px;line-height:12px;color:var(--navy)}
.news-meta{left:184px;top:917px;font-family:"Merriweather",Georgia,serif;font-size:5.5px;color:#777}
.news-body{left:149px;top:930px;width:200px;font-size:6.5px;line-height:9.5px;color:#888}
.news-more{left:149px;top:967px;font-family:"Merriweather",Georgia,serif;font-size:7.2px;color:#777}
.video{left:378px;top:889px;width:182px;height:101px;background:linear-gradient(90deg,#0b0b0b 0%,#1a1a1a 20%,#6b4a36 40%,#8b6a4e 55%,#3a2a1f 75%,#0d0d0d 100%)}
.mini-arrow{width:10px;height:10px;background:#e0e0e0;border:1px solid #ccc;display:flex;align-items:center;justify-content:center}

/* footer */
.site-footer{left:0;top:1011px;width:722px;height:189px;background:var(--footer)}
.footer-brand{left:152px;top:1022px;width:90px;color:var(--white);font-family:"Merriweather",Georgia,serif;font-size:9px;line-height:13px}
.footer-about{left:152px;top:1056px;width:132px;font-size:6.6px;line-height:9.3px;color:#8a8a8a}
.footer-title{font-family:"Merriweather",Georgia,serif;font-size:8.5px;color:#e8e8e8}
.field{background:var(--field);border-radius:1px;font-size:6.5px;color:#999;padding:3px 6px}
.footer-rule{left:149px;top:1170px;width:424px;height:1px;background:#666}
.footer-rule-accent{left:149px;top:1168px;width:60px;height:3px;background:#bbb}
.copyright{left:152px;top:1177px;font-family:"Merriweather",Georgia,serif;font-size:6.5px;color:#999}
</style>
</head>
<body>

<header class="abs site-header">
</header>
<div class="abs brand">Law Office of<br>Darnell P. Whitby</div>
<div class="abs brand-divider"></div>
<p class="abs tagline">Our goal is to balance the scales<br>through zealous advocacy.</p>
<div class="abs contact-box">
  <div><svg width="6" height="6" viewBox="0 0 10 10"><path d="M2 0l2 2-1 2c1 1.5 2 2.5 3 3l2-1 2 2-2 2C4 10 0 6 0 2z" fill="#aaa"/></svg>214.555.0186</div>
  <div><svg width="6" height="6" viewBox="0 0 10 10"><circle cx="5" cy="5" r="4.5" fill="#aaa"/></svg>releasecounsel.net</div>
</div>

<nav class="abs main-nav">
  <span class="abs nav-item active" style="left:162px">Attorney Profile</span>
  <span class="abs nav-item" style="left:235px">How We Can Help</span>
  <span class="abs nav-item" style="left:314px">Services ⌄</span>
  <span class="abs nav-item" style="left:366px">Contact Us</span>
  <div class="abs nav-bar" style="left:161px;width:59px"></div>
  <div class="abs nav-bar" style="left:310px;width:42px"></div>
</nav>

<div class="abs hero" role="img" aria-label="Photo of Dallas downtown with the Grey Stone Tribunal and autumn trees"></div>

<div class="abs dropdown">
  <div>Murder &amp; Other Homicide Offenses</div>
  <div>Sexual Offenses</div>
  <div>Expungements &amp; Non-Disclosures</div>
  <div>Early Probation Release</div>
  <div>Probation Violations</div>
  <div>Other Violent Offenses</div>
  <div>DWI, DUI</div>
  <div>Drug Offenses</div>
</div>

<div class="abs slide-arrow" style="left:549px;top:351px;background:#ddd"><svg width="5" height="6" viewBox="0 0 5 6"><path d="M4 0L1 3l3 3" stroke="#555" fill="none"/></svg></div>
<div class="abs slide-arrow" style="left:561px;top:351px;background:var(--coral)"><svg width="5" height="6" viewBox="0 0 5 6"><path d="M1 0l3 3-3 3" stroke="#fff" fill="none"/></svg></div>

<article class="abs card card-navy"><h3>Murder and other<br>homicide offenses</h3><p>Our attorneys are knowledgeable about DNA, ballistic, fingerprint, fiber analysis…</p><span>Read More</span></article>
<article class="abs card card-slate"><h3>Expungements and<br>non-disclosures</h3><p>Our lawyers help you make a fresh start through criminal record expungement …</p><span>Read More</span></article>
<article class="abs card card-coral"><h3>Early probation<br>release</h3><p>We help you put your mistakes behind you through early termination of your probation.</p><span>Read More</span></article>

<h2 class="abs section-title" style="left:149px;top:489px">Our Team</h2>
<div class="abs section-rule" style="left:149px;top:511px;width:424px"></div>
<div class="abs section-rule-accent" style="left:149px;top:509px;width:63px"></div>

<div class="abs team-card team-lead"><div class="name">Darnell P. Whitby</div><div class="role">Managing Partner</div></div>
<div class="abs team-card photo-a" role="img" aria-label="Portrait photo of a team member outdoors"></div>
<div class="abs team-card photo-b" role="img" aria-label="Portrait photo of a team member in a library office"></div>

<div class="abs team-tab active" style="top:641px">Darnell P. Whitby</div>
<div class="abs team-tab" style="top:672px">Maren Oakes-Taft</div>
<div class="abs team-tab" style="top:703px">Lyle Brandvold</div>

<h1 class="abs bio-name">Darnell P. Whitby</h1>
<p class="abs bio-text">Darnell P. Whitby is the managing partner of our law firm. Before founding his own practice, he worked for one of the best criminal defense law firms in the Dallas-Fort Worth area, where he advocated for clients accused of drug, murder, assault and other serious offenses.<br>Darnell 's lifelong career goal was to become a criminal defense trial attorney. His studies at Brazos Valley School of Law reflect his single-minded intention of honing his courtroom skills and knowledge about criminal law. Darnell won several regional advocacy contests and was runner up in multiple national competitions. His professors and peers voted for Darnell as one of the ten best advocates in the school. He earned the Judge Amos R. Pell Scholarship and a position in the honor society Lone Star Order of Advocates.</p>
<div class="abs btn" style="left:306px;top:809px;width:40px;height:13px;font-size:6.5px;line-height:13px">Read more</div>

<h2 class="abs section-title" style="left:149px;top:847px">News</h2>
<div class="abs section-rule" style="left:149px;top:869px;width:180px"></div>
<div class="abs section-rule-accent" style="left:149px;top:867px;width:63px"></div>
<div class="abs mini-arrow" style="left:332px;top:865px"><svg width="4" height="5" viewBox="0 0 4 5"><path d="M3 0L1 2.5 3 5" stroke="#555" fill="none"/></svg></div>
<div class="abs mini-arrow" style="left:343px;top:865px"><svg width="4" height="5" viewBox="0 0 4 5"><path d="M1 0l2 2.5L1 5" stroke="#555" fill="none"/></svg></div>

<h2 class="abs section-title" style="left:366px;top:847px">Our Videos</h2>
<div class="abs section-rule" style="left:366px;top:869px;width:180px"></div>
<div class="abs section-rule-accent" style="left:366px;top:867px;width:36px"></div>
<div class="abs mini-arrow" style="left:549px;top:865px"><svg width="4" height="5" viewBox="0 0 4 5"><path d="M3 0L1 2.5 3 5" stroke="#555" fill="none"/></svg></div>
<div class="abs mini-arrow" style="left:561px;top:865px"><svg width="4" height="5" viewBox="0 0 4 5"><path d="M1 0l2 2.5L1 5" stroke="#555" fill="none"/></svg></div>

<div class="abs date-box"><div class="day">27</div><div class="mon">March<br>2015</div></div>
<h3 class="abs news-title">Harlow Crane LLP gets new CEO in Owen Treadway.</h3>
<p class="abs news-meta">Colin Averett / 0 Comments</p>
<p class="abs news-body">Harlow Crane LLP, a Dallas-based law firm with a large presence in Austin and Houston, has a new CEO and board chairman in Owen Treadway.</p>
<p class="abs news-more">Read more</p>

<div class="abs video" role="img" aria-label="Embedded video of an attorney explaining expungement"></div>

<footer class="abs site-footer"></footer>
<div class="abs footer-brand">Law Office of<br>Darnell P. Whitby</div>
<p class="abs footer-about">The Law Office of Darnell P. Whitby was founded on the principle embedded in the U.S. Constitution, which states not only that all men are created equal, but that everyone is innocent until proven guilty.</p>

<h3 class="abs footer-title" style="left:296px;top:1029px">Quick Contact</h3>
<div class="abs field" style="left:296px;top:1058px;width:131px;height:16px">Name...</div>
<div class="abs field" style="left:296px;top:1079px;width:131px;height:16px">Email...</div>
<div class="abs field" style="left:296px;top:1100px;width:131px;height:34px">Message...</div>
<div class="abs btn" style="left:387px;top:1141px;width:40px;height:13px;font-size:6.5px;line-height:13px">Submit</div>

<h3 class="abs footer-title" style="left:442px;top:1029px">Newsletter</h3>
<p class="abs" style="left:442px;top:1055px;font-size:7px;color:#5e5e5e">Subscribe to our newsletter</p>
<div class="abs field" style="left:440px;top:1071px;width:133px;height:16px">Email...</div>
<div class="abs btn" style="left:533px;top:1094px;width:40px;height:13px;font-size:6.5px;line-height:13px">Subscribe</div>

<div class="abs footer-rule"></div>
<div class="abs footer-rule-accent"></div>
<p class="abs copyright">© Copyright information here</p>

</body>
</html>
```